SaaS Early tech startup business card design

Unique design for experience ecommerce platform company. the business cards will be used by executive members. conformance with color code is required.

```html
<!DOCTYPE html>
<html lang="en">
<head>
<meta charset="utf-8">
<title>Veyla Business Card</title>
<link href="https://fonts.googleapis.com/css2?family=Montserrat:wght@400;500;600;700;800&display=swap" rel="stylesheet">
<style>
  :root {
    --backdrop: #2b2b2e;
    --navy: #24243f;
    --white: #ffffff;
    --teal: #1bb89a;
    --teal-light: #4fcfaf;
    --blue: #137fa8;
    --blue-deep: #0f5f8e;
    --ink: #5a5a5e;
    --line: #6f6f73;
  }
  * { margin: 0; padding: 0; box-sizing: border-box; }
  html, body { width: 1200px; height: 900px; overflow: hidden; }
  body {
    background: var(--backdrop);
    font-family: "Montserrat", Arial, sans-serif;
    position: relative;
  }
  .card {
    position: absolute;
    top: 296px;
    width: 540px;
    height: 308px;
    border-radius: 22px;
    overflow: hidden;
  }
  .card-back { left: 40px; background: var(--navy); color: var(--white); }
  .card-front { left: 620px; background: var(--white); }
  .edge-band {
    position: absolute; left: 0; right: 0; bottom: 0; height: 14px;
    background: linear-gradient(90deg, var(--blue-deep) 0%, var(--blue) 40%, var(--teal) 70%, var(--teal-light) 100%);
  }
  .brand-name {
    font-weight: 800;
    color: var(--teal);
    letter-spacing: -1px;
    line-height: 1;
  }
  .card-back .brand-name {
    position: absolute; top: 34px; right: 58px; font-size: 64px;
  }
  .ribbon-art {
    position: absolute; right: 24px; top: 108px; width: 190px; height: 110px;
    border-radius: 40px;
    background: radial-gradient(ellipse at center, rgba(27,184,154,0.45), rgba(19,127,168,0.25) 55%, rgba(36,36,63,0) 75%);
  }
  .stat {
    position: absolute; left: 34px; bottom: 44px;
  }
  .stat-figure {
    font-size: 48px; font-weight: 500; color: var(--teal); line-height: 1;
  }
  .stat-text {
    margin-top: 6px; font-size: 17px; font-weight: 500; line-height: 1.25;
  }
  .card-front .brand-name {
    position: absolute; top: 44px; left: 0; right: 0; text-align: center; font-size: 72px;
  }
  .identity {
    position: absolute; top: 150px; left: 34px; width: 220px; text-align: right;
  }
  .person-name { font-size: 23px; font-weight: 700; color: var(--teal); }
  .person-role { font-size: 15px; font-weight: 500; color: var(--ink); margin-top: 2px; }
  .divider {
    position: absolute; top: 144px; left: 272px; width: 1.5px; height: 70px; background: var(--line);
  }
  .contacts {
    position: absolute; top: 140px; left: 290px; list-style: none;
  }
  .contacts li {
    display: flex; align-items: center; gap: 9px;
    font-size: 14.5px; color: var(--ink); height: 25px;
  }
  .contact-icon {
    width: 18px; height: 18px; border-radius: 5px; background: var(--teal);
    display: flex; align-items: center; justify-content: center; flex: none;
  }
  .address {
    position: absolute; top: 236px; left: 0; right: 0; text-align: center;
    font-size: 15px; color: var(--ink);
  }
</style>
</head>
<body>
  <section class="card card-back">
    <div class="brand-name">veyla</div>
    <div class="ribbon-art" role="img" aria-label="Soft teal and blue looping ribbon line decoration"></div>
    <div class="stat">
      <div class="stat-figure">63%</div>
      <p class="stat-text">Of Consumer Value<br>Privacy Over Popularity<br>When Dealing With<br>Online Platfrom</p>
    </div>
    <div class="edge-band"></div>
  </section>

  <section class="card card-front">
    <div class="brand-name">veyla</div>
    <div class="identity">
      <div class="person-name">Jonathan Smith</div>
      <div class="person-role">Manager</div>
    </div>
    <div class="divider"></div>
    <ul class="contacts">
      <li>
        <span class="contact-icon">
          <svg width="11" height="11" viewBox="0 0 24 24"><path fill="#fff" d="M6.6 10.8a15.1 15.1 0 0 0 6.6 6.6l2.2-2.2c.3-.3.7-.4 1-.2 1.1.4 2.3.6 3.6.6.6 0 1 .4 1 1V20c0 .6-.4 1-1 1C10.6 21 3 13.4 3 4c0-.6.4-1 1-1h3.5c.6 0 1 .4 1 1 0 1.3.2 2.5.6 3.6.1.3 0 .7-.2 1z"/></svg>
        </span>123-456-2100
      </li>
      <li>
        <span class="contact-icon">
          <svg width="12" height="10" viewBox="0 0 24 18"><rect x="1.5" y="1.5" width="21" height="15" rx="2" fill="none" stroke="#fff" stroke-width="2.5"/><path d="M2 3l10 7 10-7" fill="none" stroke="#fff" stroke-width="2.5"/></svg>
        </span>youremail@mailbox.com
      </li>
      <li>
        <span class="contact-icon">
          <svg width="12" height="12" viewBox="0 0 24 24"><circle cx="12" cy="12" r="9.5" fill="none" stroke="#fff" stroke-width="2.5"/><path d="M2.5 12h19M12 2.5c3 3 3 16 0 19M12 2.5c-3 3-3 16 0 19" fill="none" stroke="#fff" stroke-width="2"/></svg>
        </span>www.yourwebsite.com
      </li>
    </ul>
    <p class="address">Your address, city, state, ZIP 0000</p>
    <div class="edge-band"></div>
  </section>
</body>
</html>
```